Yard Sign Design Needed

Yard sign needed for mowing & landscaping company. Would like to use the top logo with black background which is attached. Would like MOWING to be in large standout letters. The word "landscaping" can be smaller and more artistic or omitted. Will need room for phone number once design is approved. The phone number will need to stand out and look identical/similar to the word 'MOWING"

```html
<!DOCTYPE html>
<html lang="en">
<head>
<meta charset="utf-8">
<title>Brennor Contractors – Mowing & Landscaping Yard Sign</title>
<link href="https://fonts.googleapis.com/css2?family=Montserrat:wght@600;800&family=Josefin+Sans:wght@300&display=swap" rel="stylesheet">
<style>
  :root {
    --ink: #0b0c0c;
    --paper: #ffffff;
    --lime: #a6cc3b;
    --lawn-light: #b3d44c;
    --lawn-dark: #9cc23c;
  }
  * { margin: 0; padding: 0; box-sizing: border-box; }
  html, body { width: 1200px; height: 960px; overflow: hidden; background: var(--paper); }
  .sign { position: relative; width: 1200px; height: 960px; background: var(--paper); overflow: hidden; }

  .brand-band {
    position: absolute; left: 0; top: 0; width: 1200px; height: 410px;
    background: var(--ink);
  }
  .brand-square {
    position: absolute; left: 545px; top: 120px; width: 110px; height: 110px;
    background: var(--lime);
  }
  .brand-name {
    position: absolute; left: 0; top: 272px; width: 1200px; text-align: center;
    font-family: "Montserrat", sans-serif; font-weight: 600; font-size: 40px;
    letter-spacing: 1px; color: var(--paper);
  }

  .headline {
    position: absolute; left: 0; top: 434px; width: 1200px; text-align: center;
    font-family: "Montserrat", sans-serif; font-weight: 800; font-size: 206px;
    line-height: 1; letter-spacing: 2px; color: var(--ink);
  }
  .subline {
    position: absolute; left: 0; top: 636px; width: 1200px; text-align: center;
    font-family: "Josefin Sans", sans-serif; font-weight: 300; font-size: 74px;
    line-height: 1; letter-spacing: 3px; color: var(--ink);
  }
  .rule { position: absolute; top: 661px; height: 4px; background: var(--lime); }
  .rule-left { left: 105px; width: 158px; }
  .rule-right { left: 935px; width: 160px; }

  .lawn-scene {
    position: absolute; left: 0; top: 712px; width: 1200px; height: 248px;
    background: linear-gradient(180deg, var(--lawn-light) 0%, var(--lawn-dark) 45%, var(--lawn-light) 100%);
  }

  .phone {
    position: absolute; left: 0; top: 777px; width: 1200px; text-align: center;
    font-family: "Montserrat", sans-serif; font-weight: 800; font-size: 146px;
    line-height: 1; letter-spacing: 0; color: var(--ink);
  }
</style>
</head>
<body>
<main class="sign">
  <header class="brand-band">
    <div class="brand-square"></div>
    <p class="brand-name">BRENNOR CONTRACTORS LLC</p>
  </header>

  <h1 class="headline">MOWING</h1>
  <span class="rule rule-left"></span>
  <p class="subline">&amp; LANDSCAPING</p>
  <span class="rule rule-right"></span>

  <div class="lawn-scene" role="img" aria-label="Illustration of rolling green lawn hills with leafy shrubs at both sides"></div>

  <p class="phone">123 456 7890</p>
</main>
</body>
</html>
```